Vellandor Insurance & Consulting

We need a new business card designed.
Front Side:
Photo on left
Logo on top right
Name, title, company, and contact info aligned on right
Clean spacing with professional hierarchy

Back Side:
Tagline centered near the top:
Real expertise. Practical guidance. Reliable protection.

Coverage types centered below in 2 lines:
General Liability | Workers Comp | Commercial Auto
Property | Inland Marine | Excess Liability | Pollution

```html
<!DOCTYPE html>
<html lang="en">
<head>
<meta charset="utf-8">
<title>Vellandor Insurance &amp; Consulting — Business Card</title>
<link href="https://fonts.googleapis.com/css2?family=Montserrat:wght@400;500;600;700&family=Oswald:wght@500&display=swap" rel="stylesheet">
<style>
  :root {
    --page: #3a3a3c;
    --card: #1f1f20;
    --card-edge: #2a2a2b;
    --ink: #ffffff;
    --ink-soft: #e4e4e4;
    --rule: #6a6a6a;
    --photo-a: #2b2b30;
    --photo-b: #4a4356;
    --photo-c: #8a6a5a;
  }
  * { box-sizing: border-box; margin: 0; padding: 0; }
  html, body { width: 1200px; height: 1200px; overflow: hidden; }
  body {
    background: var(--page);
    font-family: "Montserrat", sans-serif;
    color: var(--ink);
    display: flex;
    flex-direction: column;
    align-items: center;
    justify-content: center;
    gap: 60px;
  }
  .card {
    position: relative;
    width: 860px;
    height: 491px;
    background: radial-gradient(ellipse at 60% 40%, var(--card-edge), var(--card) 70%);
    border-radius: 34px;
    box-shadow: 0 18px 40px rgba(0,0,0,.45);
    overflow: hidden;
  }

  /* Front */
  .front .brand {
    position: absolute;
    left: 60px;
    top: 120px;
    display: flex;
    align-items: center;
    gap: 16px;
  }
  .brand-dot {
    width: 58px; height: 58px;
    border-radius: 50%;
    background: var(--ink);
    flex: none;
  }
  .brand-name {
    font-weight: 600;
    font-size: 24px;
    line-height: 1.2;
    color: var(--ink);
    max-width: 300px;
  }
  .front .rule {
    position: absolute;
    left: 60px;
    width: 420px;
    height: 1px;
    background: var(--rule);
  }
  .front .rule.top { top: 228px; }
  .front .rule.bottom { top: 342px; }
  .person {
    position: absolute;
    left: 60px;
    top: 252px;
  }
  .person-name {
    font-weight: 700;
    font-size: 32px;
    letter-spacing: .5px;
    text-transform: uppercase;
  }
  .person-title {
    font-weight: 400;
    font-size: 20px;
    letter-spacing: 1px;
    text-transform: uppercase;
    color: var(--ink-soft);
    margin-top: 4px;
  }
  .contacts {
    position: absolute;
    left: 60px;
    top: 360px;
    list-style: none;
    display: flex;
    flex-direction: column;
    gap: 8px;
  }
  .contacts li {
    display: flex;
    align-items: center;
    gap: 14px;
    font-size: 23px;
    font-weight: 500;
  }
  .contacts svg { width: 24px; height: 24px; flex: none; }
  .portrait {
    position: absolute;
    right: 60px;
    top: 30px;
    width: 330px;
    height: 461px;
    border-radius: 40% 40% 0 0 / 20% 20% 0 0;
    background: linear-gradient(180deg, var(--photo-c) 0%, var(--photo-b) 35%, var(--photo-a) 100%);
  }

  /* Back */
  .back .brand {
    position: absolute;
    left: 150px;
    top: 120px;
    display: flex;
    align-items: center;
    gap: 22px;
  }
  .back .brand-dot { width: 96px; height: 96px; }
  .back .brand-name { font-size: 38px; max-width: 480px; }
  .back .rule {
    position: absolute;
    left: 90px;
    width: 680px;
    height: 1px;
    background: var(--rule);
  }
  .back .rule.top { top: 280px; }
  .back .rule.bottom { top: 420px; }
  .tagline {
    position: absolute;
    left: 0; right: 0;
    top: 298px;
    text-align: center;
    font-weight: 700;
    font-size: 25px;
  }
  .coverage {
    position: absolute;
    left: 0; right: 0;
    top: 342px;
    text-align: center;
    font-family: "Oswald", sans-serif;
    font-weight: 500;
    font-size: 24px;
    line-height: 1.45;
    text-transform: uppercase;
  }
</style>
</head>
<body>

  <section class="card front" aria-label="Business card front">
    <div class="brand">
      <span class="brand-dot"></span>
      <span class="brand-name">Vellandor Insurance &amp; Consulting</span>
    </div>
    <div class="rule top"></div>
    <div class="person">
      <p class="person-name">Marisol Ferrante</p>
      <p class="person-title">Agency Principal</p>
    </div>
    <div class="rule bottom"></div>
    <ul class="contacts">
      <li>
        <svg viewBox="0 0 24 24" aria-hidden="true"><path fill="#fff" d="M6.6 10.8a15.1 15.1 0 0 0 6.6 6.6l2.2-2.2a1 1 0 0 1 1-.25 11.4 11.4 0 0 0 3.6.57 1 1 0 0 1 1 1V20a1 1 0 0 1-1 1A17 17 0 0 1 3 4a1 1 0 0 1 1-1h3.5a1 1 0 0 1 1 1c0 1.25.2 2.45.57 3.57a1 1 0 0 1-.25 1z"/></svg>
        (503) 555-0147
      </li>
      <li>
        <svg viewBox="0 0 24 24" aria-hidden="true"><rect x="2" y="5" width="20" height="14" rx="1" fill="#fff"/><path d="M2.5 5.5 12 13l9.5-7.5" stroke="#1f1f20" stroke-width="1.6" fill="none"/></svg>
        Admin@InsuranceMF.com
      </li>
      <li>
        <svg viewBox="0 0 24 24" aria-hidden="true" fill="none" stroke="#fff" stroke-width="1.6"><circle cx="12" cy="12" r="9.5"/><ellipse cx="12" cy="12" rx="4.2" ry="9.5"/><path d="M2.5 12h19M4 7h16M4 17h16"/></svg>
        www.VellandorInsurance.com
      </li>
    </ul>
    <div class="portrait" role="img" aria-label="Portrait photo of the agency principal"></div>
  </section>

  <section class="card back" aria-label="Business card back">
    <div class="brand">
      <span class="brand-dot"></span>
      <span class="brand-name">Vellandor Insurance &amp; Consulting</span>
    </div>
    <div class="rule top"></div>
    <p class="tagline">Real expertise. Practical guidance. Reliable protection.</p>
    <p class="coverage">
      • General Liability • Workers Comp • Commercial Auto<br>
      • Property • Inland Marine • Excess Liability • Pollution
    </p>
    <div class="rule bottom"></div>
  </section>

</body>
</html>
```